Label template request for Tarrow & Co

Project Overview:We are a handmade bath and body brand looking for an experienced packaging/label designer to create a cohesive label system for our products.

Our brand style is playful, clean, modern, bold, and slightly magical.

Scope of Work:
1. Label Template SystemDesign cohesive, print-ready templates for:
Bar soap wraps
Jar labels (scrubs, salts, creams)
Bottle labels (sprays, oils)
Small product tags
Generic shopping bag labels and stickers for shipped items.

Templates must be editable (preferably Canva-compatible) so we can update scents and product names.

Deliverables:
Print-ready files (PDF + source files)
Editable templates
Font and color specs

Ideal Candidate:
Experience with packaging/label design
Familiar with print requirements
Able to design scalable template systems
Strong portfolio of product branding work

To Apply, Please Include:

Portfolio (packaging examples preferred)
Estimated timeline
Pricing for full project
Confirmation you can provide Canva-editable files

We are looking for someone who can help create a polished, cohesive visual system for a growing product brand.

Target Market(s)

All ages, modern urban families, wide range demographics and ethnicities.

Industry/Entity Type

Soap, lotions, cosmetics

Font styles to use
Serif

Colors
FFC000
F8CF3A
FAE287
FDF2CF
FEFAEE
F0912C
F2A743
F7CA91
FBE8D2
FDF5EE
E54698
E96AAD
F1A4CE
F9D9EA
FCEFF6

Requirements
Must have
• Somewhat similar concept to example photos given, but would like you to bring your own creative ideas based on it.
Nice to have
• Water elements (flowing movement), mystical elements
Should not have
• Apothecary, farmhouse or floral style, bubbles, elegant or ornate script font

```html
<!DOCTYPE html>
<html lang="en">
<head>
<meta charset="UTF-8">
<title>Tarrow &amp; Co – Botanical Soap Label</title>
<link href="https://fonts.googleapis.com/css2?family=Cinzel:wght@400;500&display=swap" rel="stylesheet">
<style>
  :root {
    --seal-pink: #E54698;
    --band-cream: #FEFAEE;
    --band-rule: #F0912C;
    --note-ink: #E54698;
    --seal-ink: #FEFAEE;
    --sun-yellow: #FFC000;
    --butter: #FAE287;
    --butter-pale: #FDF2CF;
    --peach: #F7CA91;
    --peach-pale: #FBE8D2;
    --pink-soft: #F1A4CE;
    --pink-pale: #F9D9EA;
    --pink-mist: #FCEFF6;
  }
  * { margin: 0; padding: 0; box-sizing: border-box; }
  html, body { width: 1200px; height: 1200px; overflow: hidden; background: var(--band-cream); }
  .label {
    position: relative;
    width: 1200px;
    height: 1200px;
    overflow: hidden;
  }
  .backdrop-art {
    position: absolute;
    inset: 0;
    background:
      radial-gradient(ellipse 420px 260px at 40% 8%, var(--pink-pale) 0%, transparent 70%),
      radial-gradient(ellipse 300px 380px at 96% 24%, var(--pink-pale) 0%, transparent 70%),
      radial-gradient(ellipse 380px 300px at 8% 30%, var(--butter-pale) 0%, transparent 70%),
      radial-gradient(ellipse 420px 300px at 86% 88%, var(--peach-pale) 0%, transparent 70%),
      radial-gradient(ellipse 320px 320px at 6% 86%, var(--pink-mist) 0%, transparent 70%),
      linear-gradient(160deg, var(--pink-mist), var(--band-cream) 55%, var(--butter-pale));
  }
  .band {
    position: absolute;
    left: 0;
    top: 486px;
    width: 1200px;
    height: 224px;
    background: var(--band-cream);
    border-top: 4px solid var(--band-rule);
    border-bottom: 4px solid var(--band-rule);
  }
  .seal {
    position: absolute;
    inset: 0;
  }
  .seal-text {
    font-family: "Cinzel", serif;
    font-weight: 500;
    fill: var(--seal-ink);
  }
  .seal-text--brand { font-size: 76px; letter-spacing: 1px; }
  .seal-text--product { font-size: 64px; letter-spacing: 1px; }
  .band-note {
    position: absolute;
    top: 566px;
    width: 210px;
    font-family: "Cinzel", serif;
    font-weight: 500;
    font-size: 30px;
    line-height: 36px;
    color: var(--note-ink);
    text-align: center;
  }
  .band-note--scent { left: 105px; }
  .band-note--claim { left: 902px; }
  .hero-art {
    position: absolute;
    left: 362px;
    top: 370px;
    width: 476px;
    height: 450px;
    border-radius: 48% 52% 45% 55% / 50% 45% 55% 50%;
    background: radial-gradient(circle at 50% 40%, var(--sun-yellow) 0%, var(--sun-yellow) 7%, var(--butter) 15%, var(--peach) 40%, var(--pink-soft) 75%, var(--pink-pale) 100%);
  }
</style>
</head>
<body>
  <div class="label">
    <div class="backdrop-art" role="img" aria-label="Soft flowing watercolour wash in pastel pink, peach and butter yellow"></div>

    <svg class="seal" width="1200" height="1200" viewBox="0 0 1200 1200">
      <circle cx="600" cy="600" r="401" fill="var(--seal-pink)"/>
      <defs>
        <path id="arc-top" d="M 298 600 A 302 302 0 0 1 902 600"/>
        <path id="arc-bottom" d="M 250 600 A 350 350 0 0 0 950 600"/>
      </defs>
      <text class="seal-text seal-text--brand">
        <textPath href="#arc-top" startOffset="50%" text-anchor="middle">Tarrow &amp; Co</textPath>
      </text>
      <text class="seal-text seal-text--product">
        <textPath href="#arc-bottom" startOffset="50%" text-anchor="middle">Botanical Soap</textPath>
      </text>
    </svg>

    <div class="band"></div>

    <p class="band-note band-note--scent">Rose &amp;<br>Geranium</p>
    <p class="band-note band-note--claim">100%<br>Natural</p>

    <div class="hero-art" role="img" aria-label="Central watercolour illustration of a pastel bloom with a golden centre"></div>
  </div>
</body>
</html>
```